Corwin Tably Interiors
business card and stationary
Corwin Tably Interiors -
Creative Brief
Simple
corwin tably
interior designer
studio: 27 brookfen lane pacifica, california 94044
corwin@corwintablyinteriors.example
http://corwintablyinteriors.example
the graphic part of my logo is something i will use a lot in my branding. i like the idea of repitition or a very large version of it in a single color or grayscale that bleeds off the card.
i like the grayscale logo (white burst) on the gray background a lot. i want one side of the card to be white background, probably the front.

```html
<!DOCTYPE html>
<html lang="en">
<head>
<meta charset="utf-8">
<title>Corwin Tably Interiors – Business Card Options</title>
<link rel="stylesheet" href="https://fonts.googleapis.com/css2?family=Oswald:wght@600&family=Questrial&display=swap">
<style>
  :root {
    --page: #ecebe8;
    --label: #3b3b3b;
    --card-white: #ffffff;
    --card-gray: #8c8d90;
    --card-silver-a: #d9d9db;
    --card-silver-b: #a9aaad;
    --ink-white: #ffffff;
    --ink-gray: #6d6e71;
    --ink-dark: #4a4b4d;
    --accent-green: #9dc63f;
    --shadow: rgba(0,0,0,0.18);
  }
  * { box-sizing: border-box; margin: 0; padding: 0; }
  html, body { width: 1200px; height: 846px; overflow: hidden; }
  body {
    background: var(--page);
    font-family: "Questrial", "Century Gothic", sans-serif;
    position: relative;
  }
  .option-label {
    position: absolute; top: 28px; width: 336px; text-align: center;
    font-family: "Oswald", sans-serif; font-weight: 600; font-size: 30px;
    letter-spacing: 1px; color: var(--label);
  }
  .card {
    position: absolute; width: 336px; height: 216px; border-radius: 16px;
    box-shadow: 0 4px 10px var(--shadow); overflow: hidden;
  }
  .card--white { background: var(--card-white); }
  .card--gray { background: var(--card-gray); }
  .card--silver { background: linear-gradient(135deg, var(--card-silver-a), var(--card-silver-b)); }

  .col-1 { left: 36px; } .col-2 { left: 432px; } .col-3 { left: 828px; }
  .row-1 { top: 92px; } .row-2 { top: 336px; } .row-3 { top: 580px; }

  /* company name set as plain text */
  .brand { font-size: 19px; line-height: 1; white-space: nowrap; }
  .brand--front { position: absolute; left: 18px; top: 76px; }
  .brand--center { position: absolute; left: 0; right: 0; top: 92px; text-align: center; font-size: 22px; }
  .brand--low { top: 100px; }
  .brand--high { top: 76px; }

  .person { position: absolute; right: 18px; top: 18px; text-align: right; }
  .person__name { font-size: 15px; }
  .person__role { font-size: 9px; margin-top: 2px; }
  .address { position: absolute; right: 18px; top: 112px; text-align: right; font-size: 8px; line-height: 1.4; }
  .contact { position: absolute; right: 18px; bottom: 16px; text-align: right; font-size: 8px; line-height: 1.7; }
  .contact li { list-style: none; display: flex; justify-content: flex-end; align-items: center; gap: 5px; }
  .contact svg { width: 9px; height: 9px; }
  .url-left { position: absolute; left: 18px; bottom: 16px; font-size: 8px; }

  .url { position: absolute; left: 0; right: 0; bottom: 28px; text-align: center; font-size: 10px; }
  .url--wide { font-size: 11px; letter-spacing: 2px; bottom: 22px; }

  .ink-white { color: var(--ink-white); }
  .ink-gray { color: var(--ink-gray); }
  .ink-dark { color: var(--ink-dark); }
  .ink-green { color: var(--accent-green); }
</style>
</head>
<body>

<div class="option-label col-1">OPTION_1</div>
<div class="option-label col-2">OPTION_2</div>
<div class="option-label col-3">OPTION_3</div>

<!-- Option 1 -->
<section class="card card--gray col-1 row-1">
  <p class="brand brand--front ink-white">Corwin Tably Interiors</p>
  <div class="person"><p class="person__name ink-green">corwin tably</p><p class="person__role ink-white">interior designer</p></div>
  <p class="address ink-white">studio: 27 brookfen lane<br>halden cove, oregon 97399</p>
  <ul class="contact ink-white">
    <li>415.555.0142 <svg viewBox="0 0 10 10"><rect x="2.5" y="0.5" width="5" height="9" rx="1" fill="none" stroke="currentColor"/></svg></li>
    <li>corwin@corwintablyinteriors.example <svg viewBox="0 0 10 10"><rect x="0.5" y="2" width="9" height="6" fill="none" stroke="currentColor"/><path d="M0.5 2 L5 6 L9.5 2" fill="none" stroke="currentColor"/></svg></li>
  </ul>
</section>
<section class="card card--white col-1 row-2">
  <p class="brand brand--center ink-gray">Corwin Tably Interiors</p>
  <p class="url ink-gray">www.corwintablyinteriors.example</p>
</section>
<section class="card card--white col-1 row-3">
  <p class="brand brand--center brand--low ink-gray">Corwin Tably Interiors</p>
</section>

<!-- Option 2 -->
<section class="card card--gray col-2 row-1">
  <p class="brand brand--front ink-white">Corwin Tably Interiors</p>
  <div class="person"><p class="person__name ink-white">corwin tably</p><p class="person__role ink-white">interior designer</p></div>
  <p class="address ink-white">studio: 27 brookfen lane<br>halden cove, oregon 97399</p>
  <ul class="contact ink-white">
    <li>415.555.0142 <svg viewBox="0 0 10 10"><rect x="2.5" y="0.5" width="5" height="9" rx="1" fill="none" stroke="currentColor"/></svg></li>
    <li>corwin@corwintablyinteriors.example <svg viewBox="0 0 10 10"><rect x="0.5" y="2" width="9" height="6" fill="none" stroke="currentColor"/><path d="M0.5 2 L5 6 L9.5 2" fill="none" stroke="currentColor"/></svg></li>
    <li>www.corwintablyinteriors.example <svg viewBox="0 0 10 10"><circle cx="5" cy="5" r="4.5" fill="none" stroke="currentColor"/></svg></li>
  </ul>
</section>
<section class="card card--white col-2 row-2">
  <p class="brand brand--center ink-dark">Corwin Tably Interiors</p>
  <p class="url ink-dark">www.corwintablyinteriors.example</p>
</section>
<section class="card card--silver col-2 row-3">
  <p class="brand brand--center brand--high ink-dark">Corwin Tably Interiors</p>
  <p class="url url--wide ink-dark">www.corwintablyinteriors.example</p>
</section>

<!-- Option 3 -->
<section class="card card--white col-3 row-1">
  <p class="brand brand--front ink-gray">Corwin Tably Interiors</p>
  <div class="person"><p class="person__name ink-green">corwin tably</p><p class="person__role ink-gray">interior designer</p></div>
  <p class="address ink-gray">studio: 27 brookfen lane<br>halden cove, oregon 97399</p>
  <ul class="contact ink-gray">
    <li>415.555.0142 <svg viewBox="0 0 10 10"><rect x="2.5" y="0.5" width="5" height="9" rx="1" fill="none" stroke="currentColor"/></svg></li>
  </ul>
  <p class="url-left ink-green">www.corwintablyinteriors.example</p>
</section>
<section class="card card--gray col-3 row-2">
  <p class="brand brand--center ink-white">Corwin Tably Interiors</p>
  <p class="url ink-white">www.corwintablyinteriors.example</p>
</section>
<section class="card card--gray col-3 row-3">
  <p class="brand brand--center brand--low ink-white">Corwin Tably Interiors</p>
</section>

</body>
</html>
```